RW Frameworks Inc Business cards

We need business cards using our existing logo but slightly modified. Right now the logo says RW Framework Masonry. We want to keep the RW part of the design, but replace the Framework Masonry portion with "FRAMEWORKS". Please see the attached file.
Ideally this would be a blank template so we can add Different Names, titles, and phone numbers later.
On the one side we want only the logo and on the other side the detail. I'm attaching an example for you to see.
Please reach out with any other questions. Our address and other details will be given out once we find a design we like.

Target Market(s)

Construction Industry

```html
<!DOCTYPE html>
<html lang="en">
<head>
<meta charset="utf-8">
<title>RW Frameworks Inc – Business Cards</title>
<link rel="stylesheet" href="https://fonts.googleapis.com/css2?family=Lato:wght@700&family=Gentium+Book+Plus&display=swap">
<style>
  :root {
    --brand-blue: #1360aa;
    --brand-grey: #636467;
    --card-white: #e8e9e8;
    --page-bg: #d9dadc;
    --detail-text: #5e5f62;
  }
  * { box-sizing: border-box; margin: 0; padding: 0; }
  html, body {
    width: 1200px; height: 900px; overflow: hidden;
    background: var(--page-bg);
  }
  .canvas { position: relative; width: 1200px; height: 900px; }
  .card {
    position: absolute; left: 290px;
    width: 620px; height: 354px;
    background: var(--card-white);
    overflow: hidden;
    box-shadow: 0 6px 18px rgba(0,0,0,0.18);
  }
  .card--details { top: 60px; }
  .card--front { top: 486px; }
  .card__shapes { position: absolute; inset: 0; width: 100%; height: 100%; }
  .shape--blue { fill: var(--brand-blue); }
  .shape--grey { fill: var(--brand-grey); }

  .wordmark {
    position: absolute;
    font-family: "Lato", sans-serif;
    font-weight: 700;
    color: var(--brand-blue);
    line-height: 1;
  }
  .wordmark__initials { display: block; }
  .wordmark__name { display: block; }

  .card--front .wordmark { left: 300px; top: 100px; text-align: center; width: 250px; }
  .card--front .wordmark__initials { font-size: 112px; letter-spacing: 4px; }
  .card--front .wordmark__name { font-size: 30px; letter-spacing: 2px; margin-top: 8px; }

  .card--details .wordmark { left: 36px; top: 30px; }
  .card--details .wordmark__initials { font-size: 74px; letter-spacing: 3px; }
  .card--details .wordmark__name { font-size: 21px; letter-spacing: 1.5px; margin-top: 6px; padding-left: 40px; }

  .contact-list {
    position: absolute; left: 46px; top: 184px;
    list-style: none;
    font-family: "Gentium Book Plus", serif;
    font-size: 21px; color: var(--detail-text);
  }
  .contact-list__item { display: flex; align-items: center; gap: 20px; height: 52px; }
  .contact-list__icon { width: 40px; height: 40px; flex: none; }
  .contact-list__icon circle { fill: var(--brand-blue); }
  .contact-list__icon .glyph { fill: #ffffff; }
  .contact-list__icon .glyph-line { fill: none; stroke: var(--brand-blue); stroke-width: 1.4; }
</style>
</head>
<body>
<main class="canvas">

  <section class="card card--details" aria-label="Card back with contact details">
    <svg class="card__shapes" viewBox="0 0 350 200" preserveAspectRatio="none" aria-hidden="true">
      <path class="shape--grey" d="M282 30 C262 90 250 155 228 200 H350 V40 Z"/>
      <path class="shape--blue" d="M70 0 H350 V130 C305 65 215 18 70 0 Z"/>
    </svg>
    <div class="wordmark">
      <span class="wordmark__initials">RW</span>
      <span class="wordmark__name">FRAMEWORKS</span>
    </div>
    <ul class="contact-list">
      <li class="contact-list__item">
        <svg class="contact-list__icon" viewBox="0 0 40 40" aria-hidden="true">
          <circle cx="20" cy="20" r="20"/>
          <path class="glyph" d="M13 11 l4 -1 l3 6 l-3 2 c1 3 3 5 6 6 l2 -3 l6 3 l-1 4 c-10 0 -17 -7 -17 -17 z"/>
        </svg>
        <span>phone number</span>
      </li>
      <li class="contact-list__item">
        <svg class="contact-list__icon" viewBox="0 0 40 40" aria-hidden="true">
          <circle cx="20" cy="20" r="20"/>
          <path class="glyph" d="M20 31 C15 24 13 21 13 17 a7 7 0 0 1 14 0 c0 4 -2 7 -7 14 z"/>
          <circle cx="20" cy="17" r="2.6" style="fill: var(--brand-blue)"/>
        </svg>
        <span>location</span>
      </li>
      <li class="contact-list__item">
        <svg class="contact-list__icon" viewBox="0 0 40 40" aria-hidden="true">
          <circle cx="20" cy="20" r="20"/>
          <rect class="glyph" x="10" y="13" width="20" height="14" rx="1"/>
          <path class="glyph-line" d="M10 13 L20 21 L30 13 M10 27 L17 19 M30 27 L23 19"/>
        </svg>
        <span>e-mail address</span>
      </li>
    </ul>
  </section>

  <section class="card card--front" aria-label="Card front with company name">
    <svg class="card__shapes" viewBox="0 0 350 200" preserveAspectRatio="none" aria-hidden="true">
      <path class="shape--blue" d="M0 0 H138 C112 52 62 84 0 92 Z"/>
      <path class="shape--grey" d="M0 92 C62 102 108 150 124 200 H0 Z"/>
      <path class="shape--grey" d="M350 140 C318 182 252 200 190 200 H350 Z"/>
      <path class="shape--blue" d="M150 0 H350 V150 C322 72 245 18 150 0 Z"/>
    </svg>
    <div class="wordmark">
      <span class="wordmark__initials">RW</span>
      <span class="wordmark__name">FRAMEWORKS</span>
    </div>
  </section>

</main>
</body>
</html>
```